Quorvis Business Card

Require a business card for QuorVis. QuorVis is an aircraft engineering consultancy company.
Company is used for end of leases inspections, pre purchase inspections,asset inspections

Industry/Entity Type

Business

Contact Information for Business Card

QuorVis Limited
Miles Tandry
miles@quorvis.nz
64 (0)275918203

Requirements
Must have
• Aircraft silhouette in background

```html
<!DOCTYPE html>
<html lang="en">
<head>
<meta charset="utf-8">
<title>QuorVis Limited – Business Card</title>
<link rel="stylesheet" href="https://fonts.googleapis.com/css2?family=Montserrat:wght@500;700&family=Quicksand:wght@400;500&display=swap">
<style>
  :root {
    --page-bg: #e9e7e3;
    --card-bg: #f4f4f4;
    --ink-grey: #8d8d8d;
    --ink-dark: #7a7a7a;
    --brand-green: #22b573;
    --brand-teal: #16a99a;
    --rule-grey: #c9c9c9;
    --strip-grey: #9e9e9e;
  }
  * { margin: 0; padding: 0; box-sizing: border-box; }
  html, body {
    width: 1200px;
    height: 1000px;
    overflow: hidden;
    background: var(--page-bg);
  }
  .business-card {
    position: absolute;
    left: 100px;
    top: 215px;
    width: 1000px;
    height: 570px;
    background: radial-gradient(ellipse at 55% 35%, #ffffff 0%, var(--card-bg) 70%);
    box-shadow: 0 14px 40px rgba(0,0,0,0.18);
    overflow: hidden;
  }
  .brand-block {
    position: absolute;
    top: 110px;
    left: 0;
    width: 100%;
    text-align: center;
  }
  .brand-name {
    display: inline-flex;
    align-items: center;
    gap: 16px;
    font-family: "Montserrat", sans-serif;
    font-weight: 700;
    font-size: 54px;
    letter-spacing: 1px;
    color: var(--ink-grey);
  }
  .brand-dot {
    width: 22px;
    height: 22px;
    border-radius: 50%;
    background: var(--brand-green);
  }
  .brand-tagline {
    display: flex;
    align-items: center;
    justify-content: center;
    gap: 14px;
    margin-top: 6px;
    font-family: "Quicksand", sans-serif;
    font-weight: 500;
    font-size: 24px;
    color: var(--brand-green);
  }
  .brand-tagline::before,
  .brand-tagline::after {
    content: "";
    width: 150px;
    height: 1px;
    background: var(--rule-grey);
  }
  .contact-row {
    position: absolute;
    top: 300px;
    left: 0;
    width: 100%;
    display: flex;
    justify-content: center;
    align-items: center;
  }
  .person {
    text-align: right;
    padding-right: 26px;
  }
  .person-name {
    font-family: "Montserrat", sans-serif;
    font-weight: 700;
    font-size: 40px;
    color: var(--ink-grey);
  }
  .person-role {
    font-family: "Quicksand", sans-serif;
    font-size: 28px;
    color: var(--ink-grey);
  }
  .divider {
    width: 1px;
    height: 90px;
    background: var(--rule-grey);
  }
  .contact-list {
    list-style: none;
    padding-left: 24px;
    font-family: "Quicksand", sans-serif;
    font-size: 29px;
    color: var(--ink-dark);
  }
  .contact-list li {
    display: flex;
    align-items: center;
    gap: 10px;
    line-height: 44px;
  }
  .contact-icon { width: 26px; height: 26px; flex: none; }
  .edge-bands {
    position: absolute;
    left: 0;
    bottom: 0;
    width: 1000px;
    height: 570px;
  }
</style>
</head>
<body>
  <main class="business-card">
    <div class="brand-block">
      <div class="brand-name"><span class="brand-dot"></span>QUORVIS LIMITED</div>
      <div class="brand-tagline">Aircraft Consultants</div>
    </div>

    <section class="contact-row">
      <div class="person">
        <div class="person-name">Miles Tandry</div>
        <div class="person-role">Aircraft Consultant</div>
      </div>
      <div class="divider"></div>
      <ul class="contact-list">
        <li>
          <svg class="contact-icon" viewBox="0 0 26 26" aria-hidden="true">
            <circle cx="13" cy="13" r="13" fill="var(--brand-green)"/>
            <path d="M9 7.5c.8-.5 1.6-.3 2 .4l1 1.8c.3.6.1 1.2-.4 1.6l-.8.6c.6 1.4 1.6 2.5 3 3.2l.6-.8c.4-.5 1.1-.6 1.6-.3l1.8 1c.7.4.9 1.3.4 2-1 1.4-2.6 1.7-4.2.9-2.8-1.4-4.9-3.7-6-6.5-.5-1.6-.1-3.1 1-3.9z" fill="#fff"/>
          </svg>
          64 (0)275918203
        </li>
        <li>
          <svg class="contact-icon" viewBox="0 0 26 26" aria-hidden="true">
            <circle cx="13" cy="13" r="13" fill="var(--brand-green)"/>
            <rect x="7" y="8.5" width="12" height="9" rx="1" fill="#fff"/>
            <path d="M7.5 9.2 13 13.6l5.5-4.4" fill="none" stroke="var(--brand-green)" stroke-width="1.3"/>
          </svg>
          miles@quorvis.nz
        </li>
      </ul>
    </section>

    <svg class="edge-bands" viewBox="0 0 1000 570" aria-hidden="true">
      <defs>
        <linearGradient id="greenBand" x1="0" y1="0" x2="1" y2="0">
          <stop offset="0" stop-color="var(--brand-green)"/>
          <stop offset="0.5" stop-color="var(--brand-teal)"/>
          <stop offset="1" stop-color="var(--brand-green)"/>
        </linearGradient>
      </defs>
      <polygon class="grey-strip" points="770,478 1000,452 1000,474 820,478" fill="var(--strip-grey)"/>
      <polygon class="green-band" points="0,536 790,472 830,472 0,570" fill="url(#greenBand)"/>
    </svg>
  </main>
</body>
</html>
```